Banners - Various shapes and sizes

I need a banner set for an event planning company, www.tallowbrookoccasions.example

This will be for their Plomix Reachlink campaign, the banners can all look very similar but the final project is for a set of them, delivered as 1 PSD, in these shapes/sizes:

Mobile leaderboard: 320 x 50
Banner: 468 x 60
Leaderboard: 728 x 90
Square: 250 x 250
Small square: 200 x 200
Large rectangle: 336 x 280
Inline rectangle: 300 x 250
Skyscraper: 120 x 600
Wide skyscraper: 160 x 600
Half-page: 300 x 600
Large leaderboard: 970x90

At a minimum, they should include:

- The Bramwell Events logo
- Color scheme from their website
- Phone # and call to action

Looking over their site can provide some information on the venues, wedding packages, and awards received to get an idea of who Bramwell Events is.
Updates

Target Market(s)

Newly engaged brides

Industry/Entity Type

Event Planning

Requirements
Must have
• At a minimum, they should include:

- The Bramwell Events logo (I have attached it here)

```html
<!DOCTYPE html>
<html lang="en">
<head>
<meta charset="utf-8">
<title>Bramwell Events – Banner Set</title>
<link rel="stylesheet" href="https://fonts.googleapis.com/css2?family=Cormorant+Garamond:wght@500&family=Didact+Gothic&display=swap">
<style>
  :root{
    --canvas:#ffffff;
    --paper-top:#eed3e7;
    --paper-bottom:#e2bad8;
    --magenta:#c2268b;
    --magenta-soft:#d556a9;
    --ink:#4f4a4d;
    --white:#ffffff;
    --serif:"Cormorant Garamond", Georgia, serif;
    --sans:"Didact Gothic", Arial, sans-serif;
  }
  *{box-sizing:border-box;margin:0;padding:0}
  html,body{width:1200px;height:900px;overflow:hidden;background:var(--canvas)}
  .set{position:relative;width:1200px;height:900px}
  .banner{
    position:absolute;left:var(--x);top:var(--y);width:var(--w);height:var(--h);
    overflow:hidden;
    background:linear-gradient(180deg,var(--paper-top),var(--paper-bottom));
  }
  .rose{
    position:absolute;border-radius:50%;
    background:radial-gradient(circle at 45% 45%,var(--magenta-soft),var(--magenta) 70%);
  }
  .stack{
    position:absolute;left:0;right:0;top:var(--t);
    display:flex;flex-direction:column;align-items:center;text-align:center;
  }
  .row{position:absolute;display:flex;flex-direction:column;align-items:flex-end}
  .brand{font-family:var(--serif);font-weight:500;color:var(--magenta);line-height:1;font-size:var(--logo);white-space:nowrap}
  .tagline{font-family:var(--serif);font-weight:500;color:var(--ink);text-transform:uppercase;line-height:1.05;font-size:var(--tag);letter-spacing:-.02em;white-space:nowrap}
  .call,.prompt{font-family:var(--sans);color:var(--ink);line-height:1.25;font-size:var(--body);white-space:nowrap}
  .cta{
    display:inline-block;font-family:var(--sans);color:var(--white);background:var(--magenta);
    border-radius:4px;font-size:var(--btn);line-height:1;padding:var(--pad);text-transform:uppercase;white-space:nowrap;
  }
  .logo-mark{position:absolute;left:925px;top:50px;width:210px;height:235px}
</style>
</head>
<body>
<main class="set">

  <!-- Half-page -->
  <section class="banner" style="--x:52px;--y:0;--w:240px;--h:900px;--logo:56px;--tag:21px;--body:26px;--btn:24px;--pad:9px 22px">
    <div class="rose" role="img" aria-label="Magenta rose illustration" style="left:95px;top:-60px;width:170px;height:170px"></div>
    <div class="rose" role="img" aria-label="Magenta rose illustration" style="left:20px;top:760px;width:190px;height:190px"></div>
    <div class="stack" style="--t:200px">
      <p class="brand">Bramwell<br>Events</p>
      <p class="tagline" style="margin-top:18px">Weddings,<br>Quinces, and<br>Corporate Events</p>
      <p class="call" style="margin-top:44px">Call<br>305-555-0142<br>or</p>
      <span class="cta" style="margin-top:10px">Click Here</span>
      <p class="prompt" style="margin-top:12px">to start<br>planning<br>your event!</p>
    </div>
  </section>

  <!-- Large rectangle -->
  <section class="banner" style="--x:337px;--y:40px;--w:224px;--h:448px;--logo:30px;--tag:16px;--body:15px;--btn:15px;--pad:6px 14px">
    <div class="rose" role="img" aria-label="Magenta rose illustration" style="left:100px;top:-30px;width:110px;height:110px"></div>
    <div class="rose" role="img" aria-label="Magenta rose illustration" style="left:10px;top:335px;width:135px;height:135px"></div>
    <div class="stack" style="--t:112px">
      <p class="brand">Bramwell Events</p>
      <p class="tagline" style="margin-top:14px">Weddings, Quinces,<br>and Corporate Events</p>
      <p class="call" style="margin-top:22px">Call 305-555-0142 or</p>
      <span class="cta" style="margin-top:8px">Click Here</span>
      <p class="prompt" style="margin-top:8px">to start planning<br>your event!</p>
    </div>
  </section>

  <!-- Square -->
  <section class="banner" style="--x:573px;--y:30px;--w:250px;--h:210px;--logo:28px;--tag:14px;--body:14px;--btn:14px;--pad:5px 14px">
    <div class="rose" role="img" aria-label="Magenta rose illustration" style="left:-15px;top:110px;width:105px;height:105px"></div>
    <div class="stack" style="--t:22px;align-items:flex-start;padding-left:12px;text-align:left">
      <p class="brand">Bramwell Events</p>
      <p class="tagline" style="margin-top:8px;padding-left:18px">Weddings, Quinces,<br>and Corporate Events</p>
    </div>
    <div class="stack" style="--t:108px;left:90px">
      <p class="call">Call 305-555-0142 or</p>
      <span class="cta" style="margin-top:6px">Click Here</span>
      <p class="prompt" style="margin-top:6px">to start planning<br>your event!</p>
    </div>
  </section>

  <!-- Inline rectangle -->
  <section class="banner" style="--x:337px;--y:518px;--w:224px;--h:187px;--logo:24px;--tag:10px;--body:13px;--btn:13px;--pad:5px 12px">
    <div class="rose" role="img" aria-label="Magenta rose illustration" style="left:185px;top:-28px;width:55px;height:55px"></div>
    <div class="rose" role="img" aria-label="Magenta rose illustration" style="left:-12px;top:105px;width:85px;height:85px"></div>
    <div class="stack" style="--t:22px">
      <p class="brand" style="align-self:flex-start;padding-left:10px">Bramwell Events</p>
      <p class="tagline" style="margin-top:6px">Weddings, Quinces, and Corporate Events</p>
    </div>
    <div class="stack" style="--t:86px;left:80px">
      <p class="call">Call 305-555-0142 or</p>
      <span class="cta" style="margin-top:6px">Click Here</span>
      <p class="prompt" style="margin-top:6px">to start planning<br>your event!</p>
    </div>
  </section>

  <!-- Wide skyscraper -->
  <section class="banner" style="--x:581px;--y:258px;--w:117px;--h:447px;--logo:26px;--tag:11px;--body:13px;--btn:13px;--pad:5px 11px">
    <div class="rose" role="img" aria-label="Magenta rose illustration" style="left:25px;top:-25px;width:80px;height:80px"></div>
    <div class="rose" role="img" aria-label="Magenta rose illustration" style="left:12px;top:372px;width:92px;height:92px"></div>
    <div class="stack" style="--t:100px">
      <p class="brand">Bramwell<br>Events</p>
      <p class="tagline" style="margin-top:10px">Weddings,<br>Quinces, and<br>Corporate Events</p>
      <p class="call" style="margin-top:22px">Call<br>305-555-0142<br>or</p>
      <span class="cta" style="margin-top:4px">Click Here</span>
      <p class="prompt" style="margin-top:8px">to start<br>planning<br>your event!</p>
    </div>
  </section>

  <!-- Skyscraper -->
  <section class="banner" style="--x:724px;--y:256px;--w:89px;--h:449px;--logo:21px;--tag:8.5px;--body:13px;--btn:10px;--pad:5px 7px">
    <div class="rose" role="img" aria-label="Magenta rose illustration" style="left:10px;top:-25px;width:75px;height:75px"></div>
    <div class="rose" role="img" aria-label="Magenta rose illustration" style="left:2px;top:378px;width:82px;height:82px"></div>
    <div class="stack" style="--t:102px">
      <p class="brand">Bramwell<br>Events</p>
      <p class="tagline" style="margin-top:10px">Weddings,<br>Quinces, and<br>Corporate Events</p>
      <p class="call" style="margin-top:22px">Call<br>305-555-<br>0142 or</p>
      <span class="cta" style="margin-top:6px">Click Here</span>
      <p class="prompt" style="margin-top:10px">to start<br>planning<br>your event!</p>
    </div>
  </section>

  <!-- Small square -->
  <section class="banner" style="--x:824px;--y:250px;--w:149px;--h:148px;--logo:18px;--tag:9px;--body:10px;--btn:10px;--pad:3px 9px">
    <div class="rose" role="img" aria-label="Magenta rose illustration" style="left:-10px;top:82px;width:62px;height:62px"></div>
    <div class="stack" style="--t:12px">
      <p class="brand">Bramwell Events</p>
      <p class="tagline" style="margin-top:4px">Weddings, Quinces,<br>and Corporate Events</p>
    </div>
    <div class="stack" style="--t:74px;left:40px">
      <p class="call">Call 305-555-0142 or</p>
      <span class="cta" style="margin-top:4px">Click Here</span>
      <p class="prompt" style="margin-top:4px">to start planning<br>your event!</p>
    </div>
  </section>

  <!-- Square 250 -->
  <section class="banner" style="--x:824px;--y:410px;--w:186px;--h:186px;--logo:24px;--tag:12px;--body:12px;--btn:13px;--pad:5px 12px">
    <div class="rose" role="img" aria-label="Magenta rose illustration" style="left:-10px;top:105px;width:82px;height:82px"></div>
    <div class="stack" style="--t:18px">
      <p class="brand">Bramwell Events</p>
      <p class="tagline" style="margin-top:6px">Weddings, Quinces,<br>and Corporate Events</p>
    </div>
    <div class="stack" style="--t:96px;left:60px">
      <p class="call">Call 305-555-0142 or</p>
      <span class="cta" style="margin-top:6px">Click Here</span>
      <p class="prompt" style="margin-top:6px">to start planning<br>your event!</p>
    </div>
  </section>

  <!-- Mobile leaderboard -->
  <section class="banner" style="--x:824px;--y:610px;--w:238px;--h:36px;--logo:14px;--tag:6px;--body:7px;--btn:6.5px;--pad:2px 6px">
    <div class="rose" role="img" aria-label="Magenta rose illustration" style="left:-6px;top:6px;width:20px;height:20px"></div>
    <div class="rose" role="img" aria-label="Magenta rose illustration" style="left:120px;top:-10px;width:18px;height:18px"></div>
    <div class="row" style="left:17px;top:5px;align-items:flex-start">
      <p class="brand">Bramwell Events</p>
      <p class="tagline" style="margin-top:3px">Weddings, Quinces, and Corporate Events</p>
    </div>
    <div class="row" style="right:8px;top:5px;align-items:center">
      <p class="call">Call 305-555-0142 or</p>
      <span class="cta" style="margin-top:3px">Click Here</span>
    </div>
  </section>

  <!-- Banner -->
  <section class="banner" style="--x:824px;--y:660px;--w:350px;--h:44px;--logo:19px;--tag:9px;--body:10px;--btn:9px;--pad:3px 8px">
    <div class="rose" role="img" aria-label="Magenta rose illustration" style="left:-8px;top:12px;width:30px;height:30px"></div>
    <div class="rose" role="img" aria-label="Magenta rose illustration" style="left:210px;top:-12px;width:26px;height:26px"></div>
    <div class="row" style="left:24px;top:5px;align-items:center">
      <p class="brand">Bramwell Events</p>
      <p class="tagline" style="margin-top:2px">Weddings, Quinces, and Corporate Events</p>
    </div>
    <div class="row" style="right:14px;top:5px;align-items:center">
      <p class="call">Call 305-555-0142 or</p>
      <span class="cta" style="margin-top:3px">Click Here</span>
    </div>
  </section>

  <!-- Large leaderboard -->
  <section class="banner" style="--x:337px;--y:721px;--w:723px;--h:67px;--logo:30px;--tag:15px;--body:16px;--btn:15px;--pad:5px 16px">
    <div class="rose" role="img" aria-label="Magenta rose illustration" style="left:-10px;top:5px;width:72px;height:72px"></div>
    <div class="rose" role="img" aria-label="Magenta rose illustration" style="left:380px;top:-30px;width:55px;height:55px"></div>
    <div class="rose" role="img" aria-label="Magenta rose illustration" style="left:672px;top:5px;width:68px;height:68px"></div>
    <div class="row" style="left:105px;top:8px;align-items:flex-end">
      <p class="brand" style="align-self:flex-start">Bramwell Events</p>
      <p class="tagline" style="margin-top:3px;padding-left:45px">Weddings, Quinces, and Corporate Events</p>
    </div>
    <div class="row" style="left:510px;top:9px;align-items:center">
      <p class="call">Call 305-555-0142 or</p>
      <span class="cta" style="margin-top:5px">Click Here</span>
    </div>
  </section>

  <!-- Leaderboard -->
  <section class="banner" style="--x:337px;--y:804px;--w:543px;--h:66px;--logo:24px;--tag:12px;--body:13px;--btn:13px;--pad:5px 12px">
    <div class="rose" role="img" aria-label="Magenta rose illustration" style="left:-10px;top:5px;width:58px;height:58px"></div>
    <div class="rose" role="img" aria-label="Magenta rose illustration" style="left:300px;top:-22px;width:45px;height:45px"></div>
    <div class="rose" role="img" aria-label="Magenta rose illustration" style="left:496px;top:15px;width:55px;height:55px"></div>
    <div class="row" style="left:52px;top:10px;align-items:flex-end">
      <p class="brand" style="align-self:flex-start;padding-left:26px">Bramwell Events</p>
      <p class="tagline" style="margin-top:4px">Weddings, Quinces, and Corporate Events</p>
    </div>
    <div class="row" style="left:375px;top:12px;align-items:center">
      <p class="call">Call 305-555-0142 or</p>
      <span class="cta" style="margin-top:5px">Click Here</span>
    </div>
  </section>

  <!-- Brand rose artwork -->
  <div class="rose logo-mark" role="img" aria-label="Large magenta rose illustration"></div>

</main>
</body>
</html>
```